Webdesign für Finanzberatung
Sehr schönes Design. Auf Änderungswünsche wurde sehr schnell reagiert. Bin sehr zufrieden!
Zielgruppe
Ganzheitliche Finanzberatung / Finanzcoaching (Geldanlage, Investment, ETFs, Fonds, Aktien) für eine digital affine Zielgruppe. Es handelt sich um eine Beratung / um ein Coaching gegen Honorar.
Aufgabenstellung
Die Webseite sollte die Elemente 'digital' (Roboter) und 'persönlich' (Mensch) kombinieren. Das Design sollte modern sein und eine digital affine Zielgruppe ansprechen. Gleichzeitig soll das Thema 'persönliche Finanzberatung' zum Ausdruck gebracht werden.

```html
<!DOCTYPE html>
<html lang="de">
<head>
<meta charset="utf-8">
<title>Sorgwert Finanzen – Finanzcoaching</title>
<link href="https://fonts.googleapis.com/css2?family=Roboto:wght@300;400;500;700&display=swap" rel="stylesheet">
<style>
:root{
  --navy:#0b1633;
  --blue:#3d6b9b;
  --blue-dark:#2f5a88;
  --blue-btn:#2b64a8;
  --ink:#222a33;
  --text:#444b55;
  --light:#f3f4f5;
  --card:#eceff2;
  --rule:#c5d2e0;
  --white:#ffffff;
}
*{box-sizing:border-box;margin:0;padding:0}
html,body{width:1200px;height:3999px;overflow:hidden}
body{font-family:'Roboto',sans-serif;color:var(--text);background:var(--white);position:relative}
.abs{position:absolute}
.btn{display:inline-flex;align-items:center;gap:8px;border-radius:16px;font-size:11px;padding:0 16px;height:28px;color:var(--white);background:var(--blue-dark);text-decoration:none;white-space:nowrap}
.btn.ghost{background:transparent;border:1px solid var(--white)}
.btn svg{width:12px;height:8px}
.brand{display:flex;align-items:center;gap:10px;color:var(--white);font-weight:500;letter-spacing:2px}
.brand .dot{width:30px;height:30px;border:2px solid var(--white);border-radius:50%}

/* hero */
.hero{left:0;top:0;width:1200px;height:520px;background:linear-gradient(100deg,#070f28 0%,#0d1d45 45%,#13306b 75%,#0a1633 100%)}
.hero-art{left:560px;top:0;width:640px;height:450px;background:radial-gradient(ellipse at 70% 45%,rgba(230,120,70,.55),rgba(40,90,170,.35) 45%,rgba(10,20,50,0) 75%)}
.nav{left:0;top:56px;width:1200px;height:20px;font-size:12px;font-weight:500;color:var(--white)}
.nav span{position:absolute}
.nav .cta{background:var(--blue-btn);border-radius:14px;padding:6px 16px;top:-6px}
.hero h2{font-size:14px;font-weight:700;color:var(--white)}
.hero p{font-size:12px;color:#d5dbe6}
.wave-top{left:0;top:430px;width:1200px;height:100px}

/* heads */
.kicker{width:1200px;text-align:center;color:var(--blue);font-size:20px;font-weight:400}
.heading{width:1200px;text-align:center;color:var(--ink);font-size:25px;font-weight:700}
.divider{left:570px;width:60px;height:2px;background:var(--rule)}

/* solution */
.sol{box-shadow:0 6px 24px rgba(0,0,0,.08);background:var(--white)}
.sol h3{font-size:17px;font-weight:300;color:var(--ink);line-height:22px}
.sol h3 b{font-weight:500}
.sol p{font-size:8px;line-height:12px;color:var(--text)}
.ticks{list-style:none;font-size:8px;line-height:17px;color:var(--ink)}
.ticks li::before{content:"✓";color:var(--blue);margin-right:8px}

/* pricing */
.price{width:255px;height:360px;background:linear-gradient(120deg,#e3e8ee,#f7f8f9);padding:28px 14px}
.price.hl{background:var(--blue)}
.price h4{font-size:13px;font-weight:500;color:var(--blue);line-height:18px}
.price .amt{font-size:16px;color:var(--ink);margin:2px 0 22px 3px}
.price p{font-size:8.5px;font-weight:500;line-height:12px;margin-bottom:20px;color:var(--text)}
.price .ticks{font-size:8.5px;color:var(--text)}
.price.hl h4,.price.hl .amt,.price.hl p,.price.hl .ticks,.price.hl .ticks li::before{color:var(--white)}
.price .btn{position:absolute;bottom:48px;left:76px;height:28px;background:var(--blue-dark)}
.price.hl .btn{background:transparent;border:1px solid var(--white)}

/* why */
.why{left:0;top:2032px;width:1200px;height:570px;background:var(--blue)}
.feat{left:622px;width:360px}
.feat h5{color:#bfe0ff;font-size:12px;font-weight:400;margin-left:48px}
.feat p{color:var(--white);font-size:8px;line-height:12px;margin-left:48px;margin-top:4px}
.feat svg{position:absolute;left:0;top:2px}

/* news */
.news{width:224px;height:356px;background:var(--card);border-radius:4px;overflow:hidden}
.news .img{height:142px;background:linear-gradient(135deg,#6d7f92,#c7ccd2)}
.news .date{position:absolute;right:18px;top:118px;width:36px;height:40px;background:var(--blue-dark);color:var(--white);font-size:9px;text-align:center;padding-top:6px;line-height:11px}
.news .cat{font-size:8px;color:var(--blue);margin:22px 0 0 18px;display:flex;align-items:center;gap:6px}
.news h6{font-size:13px;font-weight:500;color:var(--ink);margin:12px 18px 0;line-height:16px}
.news p{font-size:8px;line-height:12px;margin:12px 18px 0;color:var(--text)}
.news .arr{position:absolute;left:24px;bottom:28px;width:40px;height:24px;border-radius:12px;background:var(--blue-dark);display:flex;align-items:center;justify-content:center}

/* contact */
.contact{left:0;top:3270px;width:1200px;height:460px;background:var(--light)}
.cbox{background:var(--blue);color:var(--white)}
.cbox h6{font-size:17px;font-weight:400}
.cbox small{font-size:9px;display:block;margin-top:2px}
.field{font-size:9px;color:var(--blue);border-bottom:1px solid #9aa4ae;height:24px}

.footer{left:0;top:3690px;width:1200px;height:309px}
.fnav{top:3815px;width:1200px;text-align:center;font-size:10px;font-weight:500;color:var(--white)}
.fnav span{margin:0 9px}
</style>
</head>
<body>

<!-- HERO -->
<section class="abs hero">
  <div class="abs hero-art" role="img" aria-label="Digitale Illustration: Hand mit leuchtendem Netzwerk, Pfeile auf eine Zielscheibe"></div>
  <div class="abs brand" style="left:172px;top:22px;flex-direction:column;gap:4px">
    <span class="dot" style="width:40px;height:40px"></span>
    <span style="font-size:20px">SORGWERT</span>
    <span style="font-size:8px;letter-spacing:3px">FINANZEN</span>
  </div>
  <nav class="abs nav">
    <span style="left:458px">STARTSEITE</span>
    <span style="left:567px">MEIN ANGEBOT</span>
    <span style="left:673px">ÜBER MICH</span>
    <span style="left:776px">BLOG</span>
    <span style="left:835px">KONTAKT</span>
    <span class="cta" style="left:908px">ERSTGESPRÄCH</span>
  </nav>
  <h2 class="abs" style="left:174px;top:195px">DEIN FINANZÜBERBLICK AUS EINER HAND</h2>
  <p class="abs" style="left:174px;top:213px">#FinanzenDigitalisieren #FinanzenAutomatisieren</p>
  <h2 class="abs" style="left:174px;top:247px">NACHHALTIGE FINANZENTSCHEIDUNGEN DURCH PERSÖNLICHES COACHING</h2>
  <p class="abs" style="left:174px;top:266px">#Finanzwissen #SorgwertFinanzen #FinanzielleGesundheit</p>
  <a class="abs btn" style="left:174px;top:308px;background:var(--blue-btn);height:30px;font-weight:500">ERSTGESPRÄCH BUCHEN</a>
</section>
<svg class="abs wave-top" viewBox="0 0 1200 100" preserveAspectRatio="none">
  <path d="M0 65 C250 115 500 30 800 15 C1000 5 1120 25 1200 60 L1200 100 L0 100Z" fill="#fff"/>
  <path d="M0 65 C250 115 500 30 800 15 C1000 5 1120 25 1200 60" fill="none" stroke="#2f5a88" stroke-width="3"/>
</svg>

<!-- LÖSUNG -->
<div class="abs kicker" style="top:542px">LÖSUNG</div>
<div class="abs heading" style="top:571px">VERBINDUNG VON</div>

<div class="abs sol" style="left:174px;top:646px;width:851px;height:674px"></div>
<div class="abs" role="img" aria-label="Foto: Laptop mit digitalen Finanzsymbolen" style="left:174px;top:646px;width:425px;height:337px;background:linear-gradient(135deg,#2b2f36 0%,#9aa4ae 60%,#e4d6c6 100%)"></div>
<div class="abs sol" style="left:599px;top:646px;width:426px;height:337px;box-shadow:none;padding:46px 40px">
  <h3>Automatisierung von<br><b>Finanzen mittels digitalen</b></h3>
  <p style="margin-top:18px">Lorem ipsum dolor sit amet, consectetur adipiscing elit, sed do eiusmod tempor incididunt ut labore et dolore magna aliqua. Ut enim ad minim veniam quis nostrud exercitation ullamco laboris nisi ut aliquip ex ea commodo consequat. Duis aute irure dolor in reprehenderit in voluptate velit esse cillum dolore eu fugiat nulla pariatur. Excepteur sint occaecat cupidatat non proident, sunt culpa qui officia deserunt mollit anim id est laborum.</p>
  <p style="margin-top:12px">Lorem ipsum dolor sit amet, consectetur adipiscing elit, sed do eiusmod tempor incididunt ut labore et dolore magna aliqua. Ut enim ad minim veniam quis nostrud exercitation ullamco laboris nisi ut aliquip ex ea commodo consequat.</p>
  <a class="btn" style="margin-top:18px">Weiterlesen <svg viewBox="0 0 12 8"><path d="M0 4H11M8 1l3 3-3 3" stroke="#fff" fill="none"/></svg></a>
</div>
<div class="abs sol" style="left:174px;top:983px;width:425px;height:337px;box-shadow:none;padding:44px 42px">
  <h3>persönliche Beratung bei<br><b>Finanzentscheidungen</b></h3>
  <p style="margin-top:16px">Lorem ipsum dolor sit amet, consectetur adipiscing elit, sed do eiusmod tempor incididunt ut labore et dolore magna aliqua. Ut enim ad minim veniam quis nostrud exercitation ullamco laboris nisi ut aliquip ex ea commodo consequat.</p>
  <ul class="ticks" style="margin-top:12px">
    <li>Proin a nulla ut purus efficitur vestibulum.</li>
    <li>Nam bibendum ex ut aliquet vulputate.</li>
    <li>Donec id dolor non nisi pellentesque lacinia.</li>
    <li>Fusce efficitur velit ac enim tempus, non pulvinar tortor fermentum.</li>
  </ul>
  <a class="btn" style="margin-top:18px">Weiterlesen <svg viewBox="0 0 12 8"><path d="M0 4H11M8 1l3 3-3 3" stroke="#fff" fill="none"/></svg></a>
</div>
<div class="abs" role="img" aria-label="Foto: Beratungsgespräch zwischen Berater und Kundin am Tisch" style="left:599px;top:983px;width:426px;height:337px;background:linear-gradient(135deg,#d9dde2,#8a96a3 55%,#263244)"></div>

<!-- ANGEBOT -->
<div class="abs divider" style="top:1422px"></div>
<div class="abs kicker" style="top:1451px">ANGEBOT</div>
<div class="abs heading" style="top:1480px">WÄHLEN SIE DAS BESTE ANGEBOT</div>

<div class="abs price" style="left:211px;top:1563px">
  <h4>DAS MINIMAL<br>FUNKTIONSFÄHIGES PORTFOLIO</h4><div class="amt">ab 50€</div>
  <p>Sed ut perspiciatis unde omnis iste natus error sit voluptatem rem aperiam accusantium dolorem-que laudantium.</p>
  <ul class="ticks"><li>Suspendisse mattis dui nec commodo aliquam.</li><li>Proin a nulla ut purus efficitur vestibulum.</li><li>Nam bibendum ex ut aliquet vulputate.</li><li>Donec id dolor non nisi pellentesque lacinia.</li></ul>
  <a class="btn">Weiterlesen <svg viewBox="0 0 12 8"><path d="M0 4H11M8 1l3 3-3 3" stroke="#fff" fill="none"/></svg></a>
</div>
<div class="abs price hl" style="left:473px;top:1563px">
  <h4>FINANZPLAN &amp;<br>VERMÖGENSMANAGEMENT</h4><div class="amt">ab 600€</div>
  <p>Sed ut perspiciatis unde omnis iste natus error sit voluptatem rem aperiam accusantium dolorem-que laudantium.</p>
  <ul class="ticks"><li>Suspendisse mattis dui nec commodo aliquam.</li><li>Proin a nulla ut purus efficitur vestibulum.</li><li>Nam bibendum ex ut aliquet vulputate.</li><li>Donec id dolor non nisi pellentesque lacinia.</li></ul>
  <a class="btn">Weiterlesen <svg viewBox="0 0 12 8"><path d="M0 4H11M8 1l3 3-3 3" stroke="#fff" fill="none"/></svg></a>
</div>
<div class="abs price" style="left:735px;top:1563px">
  <h4>INDIVIDUELLES COACHING<br>&amp; BERATUNG</h4><div class="amt">ab 400€</div>
  <p>Sed ut perspiciatis unde omnis iste natus error sit voluptatem rem aperiam accusantium dolorem-que laudantium.</p>
  <ul class="ticks"><li>Suspendisse mattis dui nec commodo aliquam.</li><li>Proin a nulla ut purus efficitur vestibulum.</li><li>Nam bibendum ex ut aliquet vulputate.</li><li>Donec id dolor non nisi pellentesque lacinia.</li></ul>
  <a class="btn">Weiterlesen <svg viewBox="0 0 12 8"><path d="M0 4H11M8 1l3 3-3 3" stroke="#fff" fill="none"/></svg></a>
</div>

<!-- WARUM -->
<section class="abs why">
  <svg class="abs" style="left:0;top:0" width="600" height="570" viewBox="0 0 600 570">
    <path d="M0 0H370 A420 420 0 0 1 420 570 H0Z" fill="#d8dde3"/>
    <path d="M370 0 A420 420 0 0 1 420 570" fill="none" stroke="#5b8fc7" stroke-width="6"/>
  </svg>
  <div class="abs" role="img" aria-label="Porträtfoto des Finanzcoaches im Sakko" style="left:0;top:0;width:420px;height:570px;background:linear-gradient(160deg,#c9cfd6,#7c8896 60%,#1e2a3d);clip-path:path('M0 0H367 A417 417 0 0 1 417 570 H0Z')"></div>
  <div class="abs" style="left:630px;top:56px;color:var(--white);font-size:11px">WARUM UNS WÄHLEN</div>
  <div class="abs" style="left:630px;top:72px;color:var(--white);font-size:24px;font-weight:700;line-height:34px">SEIT ÜBER 20 JAHREN IM<br>BEREICH FINANZEN</div>
  <p class="abs" style="left:630px;top:148px;width:330px;color:var(--white);font-size:9px;line-height:13px">Lorem ipsum dolor sit amet, consectetur adipiscing elit, sed do eiusmod tempor incididunt ut labore et dolore magna aliqua. Ut enim ad minim veniam, quis nostrud exercitation ullamco laboris nisi ut aliquip ex ea com-modo consequat.</p>
  <div class="abs feat" style="top:240px"><svg width="38" height="38" viewBox="0 0 38 38"><circle cx="19" cy="19" r="15" fill="none" stroke="#bfe0ff" stroke-width="1.5"/><circle cx="19" cy="19" r="8" fill="none" stroke="#bfe0ff" stroke-width="1.5"/><path d="M19 19L33 5" stroke="#bfe0ff" stroke-width="1.5"/></svg><h5>Finanzmanagement und Beratung</h5><p>Diam vel quam elementum pulvinar ac tium aenean<br>pharetra magna ac placerat quis eget.</p></div>
  <div class="abs feat" style="top:309px"><svg width="38" height="38" viewBox="0 0 38 38"><rect x="3" y="6" width="30" height="22" fill="none" stroke="#bfe0ff" stroke-width="1.5"/><path d="M8 22l6-6 5 4 8-9" stroke="#bfe0ff" fill="none" stroke-width="1.5"/><path d="M12 32h14" stroke="#bfe0ff" stroke-width="1.5"/></svg><h5>Marktforschung und -analyse</h5><p>Diam vel quam elementum pulvinar ac tium aenean<br>pharetra magna ac placerat quis eget.</p></div>
  <div class="abs feat" style="top:378px"><svg width="38" height="38" viewBox="0 0 38 38"><circle cx="13" cy="12" r="6" fill="none" stroke="#bfe0ff" stroke-width="1.5"/><circle cx="26" cy="15" r="5" fill="none" stroke="#bfe0ff" stroke-width="1.5"/><path d="M3 34c0-8 5-12 10-12s10 4 10 12M20 34c1-6 4-9 6-9s7 3 8 9" fill="none" stroke="#bfe0ff" stroke-width="1.5"/></svg><h5>Technologieberatung</h5><p>Diam vel quam elementum pulvinar ac tium aenean<br>pharetra magna ac placerat quis eget.</p></div>
  <a class="abs btn ghost" style="left:625px;top:462px;font-size:10px">ERSTGESPRÄCH BUCHEN <svg viewBox="0 0 12 8"><path d="M0 4H11M8 1l3 3-3 3" stroke="#fff" fill="none"/></svg></a>
</section>

<!-- NEWS -->
<div class="abs divider" style="top:2698px"></div>
<div class="abs kicker" style="top:2733px;font-size:14px">BLEIBEN SIE MIT LENNART VOSSKAMP AUF DEM LAUFENDEN</div>
<div class="abs heading" style="top:2750px">VON DEN NEUESTEN &amp; BELIEBTEN NEWS</div>

<article class="abs news" style="left:242px;top:2827px"><div class="img" role="img" aria-label="Foto: Industriemaschine in Nahaufnahme"></div><div class="date">July 19<br>2021</div><div class="cat"><svg width="11" height="9" viewBox="0 0 11 9"><path d="M.5 1.5h3.5l1 1h5.5v6H.5z" fill="none" stroke="#3d6b9b"/></svg>Artificial Store</div><h6>Repeated of endeavor mr position kindness.</h6><p>Lorem ipsum dolor sit amet, consectetur adipiscing elit, sed do eiusmod tempor incid-idunt ut labore.</p><span class="arr"><svg width="12" height="8" viewBox="0 0 12 8"><path d="M0 4H11M8 1l3 3-3 3" stroke="#fff" fill="none"/></svg></span></article>
<article class="abs news" style="left:487px;top:2827px"><div class="img" role="img" aria-label="Foto: Techniker in einer Fertigungshalle" style="background:linear-gradient(135deg,#3d6b9b,#d8c6a8)"></div><div class="date">July 19<br>2021</div><div class="cat"><svg width="11" height="9" viewBox="0 0 11 9"><path d="M.5 1.5h3.5l1 1h5.5v6H.5z" fill="none" stroke="#3d6b9b"/></svg>Automation</div><h6>Justifying Automation in Your Factory.</h6><p>Lorem ipsum dolor sit amet, consectetur adipiscing elit, sed do eiusmod tempor incid-idunt ut labore.</p><span class="arr"><svg width="12" height="8" viewBox="0 0 12 8"><path d="M0 4H11M8 1l3 3-3 3" stroke="#fff" fill="none"/></svg></span></article>
<article class="abs news" style="left:732px;top:2827px"><div class="img" role="img" aria-label="Foto: Roboterarm in einer Produktionsanlage" style="background:linear-gradient(135deg,#4a4f55,#cfd3d8)"></div><div class="date">July 19<br>2021</div><div class="cat"><svg width="11" height="9" viewBox="0 0 11 9"><path d="M.5 1.5h3.5l1 1h5.5v6H.5z" fill="none" stroke="#3d6b9b"/></svg>Digitalization</div><h6>Boost Your Cobot Safety Know-How with These Digital Resources</h6><p>Lorem ipsum dolor sit amet, consectetur adipiscing elit, sed do eiusmod tempor incid-idunt ut labore.</p><span class="arr"><svg width="12" height="8" viewBox="0 0 12 8"><path d="M0 4H11M8 1l3 3-3 3" stroke="#fff" fill="none"/></svg></span></article>

<!-- KONTAKT -->
<section class="abs contact">
  <div class="abs" style="left:270px;top:27px;width:222px;height:340px;background:#6b9ad1"></div>
  <div class="abs cbox" style="left:258px;top:13px;width:222px;height:340px;padding:64px 0 0 16px">
    <div style="display:flex;gap:14px"><svg width="24" height="24" viewBox="0 0 24 24"><path d="M12 2a6 6 0 0 1 6 6c0 5-6 11-6 11S6 13 6 8a6 6 0 0 1 6-6z" fill="#fff"/><circle cx="12" cy="8" r="2" fill="#3d6b9b"/></svg><div><h6>SORGWERT</h6><small>Lindenkamp 7b<br>22391 Hamburg</small></div></div>
    <div style="border-top:1px solid rgba(255,255,255,.5);width:194px;margin:12px 0 16px"></div>
    <div style="display:flex;gap:14px"><svg width="24" height="24" viewBox="0 0 24 24"><path d="M5 3l4 0 2 5-3 2c1 3 3 5 6 6l2-3 5 2v4c-9 1-17-7-16-16z" fill="#fff"/></svg><div><h6>Einen Anruf tätigen</h6><small>040 / 55501234</small></div></div>
    <div style="border-top:1px solid rgba(255,255,255,.5);width:194px;margin:30px 0 16px"></div>
    <div style="display:flex;gap:14px"><svg width="24" height="24" viewBox="0 0 24 24"><path d="M2 6h20v13H2z" fill="#fff"/><path d="M2 6l10 8 10-8" stroke="#3d6b9b" fill="none" stroke-width="1.5"/></svg><div><h6 style="font-size:14px;font-weight:500">Senden Sie eine E-Mail</h6><small>info@sorgwert.de</small></div></div>
    <div style="border-top:1px solid rgba(255,255,255,.5);width:194px;margin:30px 0 0"></div>
  </div>
  <div class="abs" style="left:537px;top:33px;font-size:11px;color:var(--blue)">WIR FREUEN UNS JEDERZEIT VON IHNEN ZU HÖREN</div>
  <div class="abs" style="left:537px;top:51px;font-size:15px;font-weight:500;color:var(--ink)">MACHEN SIE SICH BEREIT, IHR PROJEKT MIT UNS ZU STARTEN</div>
  <div class="abs field" style="left:537px;top:103px;width:413px">Name</div>
  <div class="abs field" style="left:537px;top:147px;width:188px">Email*</div>
  <div class="abs field" style="left:762px;top:147px;width:188px">Telefon</div>
  <div class="abs field" style="left:537px;top:190px;width:413px;height:100px">Erzählen Sie uns über das Projekt*</div>
  <a class="abs btn" style="left:537px;top:325px;font-size:10px">Nachricht Senden <svg viewBox="0 0 12 10" style="width:12px;height:10px"><path d="M0 5L12 0 9 10 6 6z" fill="#fff"/></svg></a>
</section>

<!-- FOOTER -->
<svg class="abs footer" viewBox="0 0 1200 309" preserveAspectRatio="none">
  <defs><linearGradient id="foot" x1="0" y1="0" x2="0" y2="1"><stop offset="0" stop-color="#3d6b9b"/><stop offset="1" stop-color="#1d3f70"/></linearGradient></defs>
  <path d="M0 22 C300 60 600 0 900 18 C1050 28 1150 10 1200 0 V309 H0Z" fill="url(#foot)"/>
</svg>
<div class="abs fnav"><span>STARTSEITE</span><span>MEIN ANGEBOT</span><span>ÜBER MICH</span><span>ÜBER UNS</span><span>BLOG</span><span>KONTAKT</span></div>
<div class="abs" style="top:3846px;width:1200px;text-align:center;font-size:9px;color:var(--white)">COPYRIGHT © 2021. ALL RIGHTS RESERVED.</div>
<div class="abs brand" style="left:0;top:3885px;width:1200px;flex-direction:column;gap:4px">
  <span class="dot" style="width:34px;height:34px"></span>
  <span style="font-size:18px">SORGWERT</span>
  <span style="font-size:7px;letter-spacing:3px">FINANZEN</span>
</div>
</body>
</html>
```